Real Estate Sign to Help Modernize and Make it POP!

Design a sign style that would be good for marketing the sale or lease of properties. This will be 3 ' x 4' when printed and needs to look professional, modern, and catchy. It should us the company name, logo, and phone number at a minimum. Keep with the color scheme but open to varieties.

It will be printed and put in a large wooden frame as shown in one of the pictures.

Target Market(s)

Buyers and Tenants

Industry/Entity Type

Real Estate

Requirements
Must have
• company name, logo, and phone number
same color scheme as sign and website
Nice to have
• My Name, "Merrick Halvane, CCIM"
Company Website
Ability to have an easy change from FOR SALE to FOR LEASE or FOR SALE/LEASE when I need to move this sign to a new property
An ability to have reflective colors printed on the contrast for cars to see at night
Should not have
• "Property Managed by"

```html
<!DOCTYPE html>
<html lang="en">
<head>
<meta charset="utf-8">
<title>Meridian Harbor Realty – For Sale Sign</title>
<link rel="stylesheet" href="https://fonts.googleapis.com/css2?family=Montserrat:wght@400;500;600;800&display=swap">
<style>
  :root {
    --brand-teal: #43645d;
    --sign-white: #ffffff;
  }
  html, body {
    margin: 0;
    padding: 0;
    width: 1200px;
    height: 919px;
    overflow: hidden;
    background: var(--sign-white);
  }
  .sign {
    position: relative;
    width: 1200px;
    height: 919px;
    overflow: hidden;
    background: var(--sign-white);
    font-family: "Montserrat", sans-serif;
    color: var(--brand-teal);
  }
  .sign h1,
  .sign p {
    margin: 0;
  }
  .corner-accents {
    position: absolute;
    inset: 0;
  }
  .brand {
    position: absolute;
    left: 0;
    right: 0;
    top: 145px;
    display: flex;
    align-items: center;
    justify-content: center;
    gap: 28px;
  }
  .brand-dot {
    width: 64px;
    height: 64px;
    border-radius: 50%;
    background: var(--brand-teal);
  }
  .brand-name {
    font-weight: 500;
    font-size: 62px;
    letter-spacing: 0.08em;
    line-height: 1;
    text-transform: uppercase;
    white-space: nowrap;
  }
  .status-band {
    position: absolute;
    left: 0;
    top: 333px;
    width: 1200px;
    height: 234px;
    background: var(--brand-teal);
    display: flex;
    align-items: center;
    justify-content: center;
  }
  .status-label {
    color: var(--sign-white);
    font-weight: 800;
    font-size: 196px;
    line-height: 1;
    letter-spacing: -0.01em;
    margin-left: 10px;
  }
  .agent {
    position: absolute;
    right: 109px;
    text-align: right;
    line-height: 1;
    white-space: nowrap;
  }
  .agent-name {
    top: 603px;
    font-weight: 600;
    font-size: 48px;
    letter-spacing: 0.5em;
    margin-right: -0.5em;
  }
  .agent-phone {
    top: 652px;
    font-weight: 800;
    font-size: 150px;
    letter-spacing: -0.01em;
  }
  .agent-web {
    top: 802px;
    font-weight: 400;
    font-size: 57px;
  }
</style>
</head>
<body>
  <main class="sign">
    <svg class="corner-accents" width="1200" height="919" viewBox="0 0 1200 919" aria-hidden="true">
      <polygon points="1059,0 1200,0 1200,143" fill="var(--brand-teal)"/>
      <polygon points="0,778 0,919 140,919" fill="var(--brand-teal)"/>
    </svg>

    <header class="brand">
      <span class="brand-dot"></span>
      <span class="brand-name">Meridian Harbor Realty</span>
    </header>

    <section class="status-band">
      <h1 class="status-label">FOR SALE</h1>
    </section>

    <p class="agent agent-name">Merrick Halvane, CCIM</p>
    <p class="agent agent-phone">985-555-0147</p>
    <p class="agent agent-web">MERIDIANHARBORREALTY.COM</p>
  </main>
</body>
</html>
```